Bref créative
The Marlowe Gala
Event Planning
Professional
Rosalind Hartwell
Owner - The Marlowe Gala
4105 - 27 Ashcombe Avenue
Toronto, ON M5R 2K7
rosalind@TheMarloweGala.example
www.TheMarloweGala.example
The card can be single or double sided i don't mind. Just be creative and make it clean!!!
Thanks!
It can be single or double sided I dont mind.

```html
<!DOCTYPE html>
<html lang="en">
<head>
<meta charset="utf-8">
<title>The Marlowe Gala – Business Card</title>
<link href="https://fonts.googleapis.com/css2?family=Arimo:wght@400;700&display=swap" rel="stylesheet">
<style>
  :root {
    --frame: #000000;
    --board: #a3a3a3;
    --paper: #ffffff;
    --slate: #5b5b5b;
    --slate-edge: #3e3e3e;
    --ink: #4a4a4a;
    --ink-soft: #6a6a6a;
    --band: #5e5e5e;
    --light: #ffffff;
  }
  * { margin: 0; padding: 0; box-sizing: border-box; }
  html, body { width: 1200px; height: 720px; overflow: hidden; background: var(--frame); }
  body { font-family: "Arimo", Arial, sans-serif; position: relative; }
  .board {
    position: absolute; left: 53px; top: 53px; width: 1094px; height: 619px;
    background: var(--board);
  }
  .card {
    position: absolute; width: 487px; height: 276px; border-radius: 24px;
    overflow: hidden;
  }
  .card--white { background: var(--paper); border: 2px solid var(--ink-soft); }
  .card--dark { background: var(--slate); border: 2px solid var(--slate-edge); }
  .card--front { left: 36px; top: 36px; }
  .card--back-a { left: 540px; top: 36px; }
  .card--back-b { left: 36px; top: 326px; }
  .card--back-c { left: 540px; top: 326px; }

  .brand { position: absolute; display: flex; align-items: center; gap: 10px; }
  .brand__square { width: 22px; height: 22px; background: currentColor; }
  .brand__name { font-size: 17px; letter-spacing: 1px; font-weight: 400; }
  .brand--corner { left: 28px; top: 18px; flex-direction: column; align-items: flex-start; gap: 6px; color: var(--ink); }
  .brand--corner .brand__square { width: 70px; height: 62px; margin-left: 40px; }
  .brand--corner .brand__name { font-size: 15px; }
  .brand__tag { position: absolute; left: 58px; top: 112px; font-size: 9px; letter-spacing: 3px; color: var(--ink-soft); }
  .brand--center { left: 0; right: 0; top: 0; bottom: 0; justify-content: center; gap: 14px; }
  .brand--center .brand__square { width: 34px; height: 34px; }
  .brand--center .brand__name { font-size: 26px; }
  .card--white .brand--center { color: var(--ink); }
  .card--dark .brand--center { color: var(--light); }

  .band { position: absolute; left: 0; top: 0; width: 487px; height: 276px; }
  .holder { position: absolute; right: 24px; top: 122px; text-align: right; color: var(--ink); }
  .holder__name { font-size: 22px; font-weight: 400; }
  .holder__role { font-size: 13px; margin-top: 4px; color: var(--ink-soft); }
  .contact { position: absolute; left: 16px; top: 174px; color: var(--light); font-size: 11px; line-height: 16.5px; }
</style>
</head>
<body>
  <main class="board">
    <section class="card card--white card--front">
      <svg class="band" viewBox="0 0 487 276" aria-hidden="true">
        <path d="M0 146 C120 150 300 176 487 196 L487 276 L0 276 Z" fill="var(--band)"/>
        <path d="M0 153 C140 158 320 184 487 202" fill="none" stroke="var(--light)" stroke-width="3"/>
      </svg>
      <div class="brand brand--corner">
        <span class="brand__square"></span>
        <span class="brand__name">THE MARLOWE GALA</span>
      </div>
      <span class="brand__tag">Event Planning</span>
      <div class="holder">
        <p class="holder__name">Rosalind Hartwell</p>
        <p class="holder__role">Owner - The Marlowe Gala</p>
      </div>
      <address class="contact" style="font-style:normal">
        4105 - 27 Ashcombe Avenue<br>
        Toronto, ON M5R 2K7<br>
        Cell: 416.555.0142 | Phone: 416.555.0187<br>
        Fax: 416.555.0163<br>
        Email: rosalind@TheMarloweGala.example<br>
        www.TheMarloweGala.example
      </address>
    </section>

    <section class="card card--dark card--back-a">
      <div class="brand brand--center">
        <span class="brand__square"></span>
        <span class="brand__name">The Marlowe Gala</span>
      </div>
    </section>

    <section class="card card--white card--back-b">
      <div class="brand brand--center">
        <span class="brand__square"></span>
        <span class="brand__name">The Marlowe Gala</span>
      </div>
    </section>

    <section class="card card--dark card--back-c">
      <div class="brand brand--center">
        <span class="brand__square"></span>
        <span class="brand__name">The Marlowe Gala</span>
      </div>
    </section>
  </main>
</body>
</html>
```